Web Design Project: Executive Coach

PLEASE check out http://tovrenly.com.sg/x/PixelHive/PixelHive_Brief/Blank.html

It is a better description of what I am after. It includes everything in this brief and in an easier format. (And...I don't have your design skills, so it doesn't look great.)

========

What the site offers
-
I am about to launch a one-person company that provides three services:
1) executive coaching
2) leadership training
3) psychotherapy to adults

My Unique Selling Point
-
My unique selling point is that I am a coach who is also a relatively senior psychologist. However, psychologists can be seen as scary and that may put people off.

The Biggest Challenge: The Target Audience
-
One challenge is that because I sell 3 services, I want to appeal to more than one demographic. They are:

1) The representative from HR of a company who wants to buy a leadership course or find a coach for an executive in the company. (Usually mid-40’s and older.)

2) The executives who will take the selection made by the head of HR and may choose me from 3 or 4 other options. (Usually late 30’s to mid 40’s. Both men and women. From multinational companies.)

3) Psychotherapy clients who are coming to be directly, not via HR, and who don’t want to feel insecure that they aren’t executives but still may be a good fit to work with me. (More women than men. Age 34-45. Typically have some European or American exposure.)

The Problem
-
The executives I see may or may not have some psychological concerns, but most will quite like that I am a psychologist as long as I’m not “scary” but “kind”. (Kind is key.) So while it is important to show I am a therapist, I don't want it to make executives embarrassed when a colleague says “Oh, I looked at this guy’s website. You aren't in therapy are you?”

As mentioned above, please check out the following link: http://tovrenly.com.sg/x/PixelHive/PixelHive_Brief/Blank.html

________
Please note, I originally posted this as 584207 Executive Coaching, Leadership Training, and Psychotherapy Website. With the help of one designer and also PixelHive customer support, I realized that I had requested only the design of a website, not the coding. I had offered the maximum amount, US$1000 (refundable). I am resubmitting the project here and I have guaranteed the funds. I am lowering the payment as I am now aware that I was only asking for design. I apologize for any inconvenience. And thank your for being interested in this project.
Updates

Project Deadline Extended
Reason: I would love to get started on the coding next week. So I hope to get your proposals in the next 3 days.

Target Market(s)

Primary audience: 34-44 year old men and women with some European / North American exposure

Industry/Entity Type

Leadership

Requirements
Must have
• Video on home page
Nice to have
• I would like have quotes slide in to a couple of the pages. These may have a photo of the author attached.

I would like Workvine integration with my business's Workvine page. (I haven't made one yet, so I'm not sure how it works.)

```html
<!DOCTYPE html>
<html lang="en">
<head>
<meta charset="utf-8">
<title>Halbrook Consulting</title>
<link rel="stylesheet" href="https://fonts.googleapis.com/css2?family=Jost:wght@400;500;600;700&family=Arimo:wght@400;700&family=Noto+Sans:wght@400;700&display=swap">
<style>
:root{
  --ink:#222;
  --grey-text:#555;
  --teal:#0f5063;
  --teal-link:#0e5a6e;
  --nav-bg:#545454;
  --panel-bg:#ebebeb;
  --footer-bg:#dadada;
  --cyan-top:#3fd0f0;
  --cyan-bottom:#12aedb;
  --network-blue:#3b5998;
  --rule:#d6d6d6;
}
*{box-sizing:border-box;margin:0;padding:0}
html,body{width:1101px;height:1200px;overflow:hidden}
body{position:relative;background:#fff;font-family:"Noto Sans",sans-serif;color:var(--ink)}
.abs{position:absolute}

/* header */
.site-header{left:0;top:0;width:1101px;height:147px;border-top:3px solid #111;background:linear-gradient(#f4f4f4,#e2e2e2)}
.brand{left:93px;top:44px;display:flex;align-items:center;gap:10px}
.brand-mark{width:60px;height:48px;background:#6e6e6e}
.brand-name{font-family:"Jost",sans-serif;font-weight:400;font-size:24px;color:#6e6e6e;letter-spacing:.3px;line-height:1}
.brand-tag{left:187px;top:87px;font-family:"Arimo",sans-serif;font-style:italic;font-size:13px;color:#555}
.social{right:50px;top:56px;display:flex;gap:18px}
.social-item{width:34px;height:34px;background:#111;color:#fff;font-family:"Arimo",sans-serif;font-size:7px;display:flex;align-items:flex-end;justify-content:center;padding-bottom:3px;box-shadow:0 6px 4px -4px rgba(0,0,0,.25)}

/* nav */
.main-nav{left:0;top:147px;width:1101px;height:56px;background:var(--nav-bg);display:flex;justify-content:center;align-items:center;font-family:"Arimo",sans-serif;font-size:15px;color:#fff;letter-spacing:.5px}
.main-nav span{padding:0 15px}
.main-nav .sep{padding:0}

/* welcome panel */
.welcome{left:47px;top:215px;width:1007px;height:313px;background:var(--panel-bg);border:1px solid #ddd;border-radius:4px;box-shadow:0 1px 4px rgba(0,0,0,.2)}
.welcome-title{left:116px;top:236px;font-family:"Jost",sans-serif;font-weight:600;font-size:64px;color:var(--teal);line-height:1.1}
.welcome-sub{left:116px;top:311px;font-family:"Arimo",sans-serif;font-size:18px;color:#555}
.welcome-copy{left:116px;top:348px;width:338px;font-size:13px;line-height:20.5px;color:#555}
.btn-more{left:116px;top:448px;width:155px;height:40px;border-radius:3px;background:linear-gradient(var(--cyan-top),var(--cyan-bottom));color:#fff;font-family:"Arimo",sans-serif;font-weight:700;font-size:14px;display:flex;align-items:center;justify-content:center;gap:8px}
.video-bar{left:621px;top:230px;width:375px;height:29px;background:#1b1b1b;border-radius:4px 4px 0 0;color:#fff;font-family:"Jost",sans-serif;font-weight:500;font-size:18px;padding:2px 12px}
.video{left:621px;top:262px;width:375px;height:248px;background:#000}
.video-frame{left:621px;top:283px;width:375px;height:202px;background:linear-gradient(100deg,#7a6b55,#b7a58a 45%,#8c7c62 70%,#c9c0b0)}
.video-caption{left:632px;top:267px;font-family:"Arimo",sans-serif;font-size:10px;color:#eee}
.video-controls{left:621px;top:486px;width:375px;height:24px;background:linear-gradient(#2c2c2c,#151515);color:#ccc;font-family:"Arimo",sans-serif;font-size:9px}

/* left column */
.col-title{font-family:"Jost",sans-serif;font-weight:500;font-size:19px;color:#222}
.like-row{left:62px;top:594px;display:flex;align-items:center;gap:7px;font-family:"Arimo",sans-serif;font-size:11px;color:#333}
.like-btn{border:1px solid #bbb;border-radius:2px;background:#eef0f5;padding:2px 6px;color:var(--network-blue)}
.network-square{width:11px;height:11px;background:var(--network-blue)}
.activity{left:64px;top:629px;width:307px;height:358px;border:1px solid #999;font-family:"Arimo",sans-serif}
.activity-head{height:33px;background:#eceff5;border-bottom:1px solid #ccc;font-weight:700;font-size:13px;padding:9px 10px}
.login-row{display:flex;gap:10px;padding:10px 6px 10px 10px;margin:0 6px;border-bottom:1px solid #ccc;font-size:11px;color:#666;line-height:14px}
.login-btn{background:#5b74a8;border:1px solid #29447e;color:#fff;font-weight:700;font-size:12px;padding:4px 6px;height:25px}
.act-item{display:flex;gap:10px;padding:8px 10px 4px;font-size:11px;color:#777;line-height:14px}
.act-icon{width:32px;height:32px;flex:none}
.act-item b{display:block;color:#3b5998;font-size:11.5px}
.plugin-foot{position:absolute;left:6px;right:6px;bottom:6px;border-top:1px solid #ccc;padding-top:6px;font-size:10px;color:#666;display:flex;gap:6px;align-items:center}
.divider{left:401px;top:560px;width:1px;height:480px;background:var(--rule)}

/* services */
.service-img{width:176px;height:106px;border:3px solid #fff;border-radius:3px;box-shadow:0 1px 4px rgba(0,0,0,.3)}
.service-blurb{font-size:13px;color:var(--teal-link);line-height:15px;width:400px}
.service-copy{font-size:13px;line-height:15px;color:#111;width:405px}

/* footer */
.site-footer{left:0;top:1080px;width:1101px;height:120px;background:var(--footer-bg);text-align:center;font-size:13px;color:#555}
.site-footer p{margin-top:40px}
.footer-links{margin-top:10px;color:var(--teal)}
</style>
</head>
<body>

<header class="abs site-header"></header>
<div class="abs brand"><span class="brand-mark"></span><span class="brand-name">HALBROOK CONSULTING</span></div>
<div class="abs brand-tag">Transforming teams, leaders, and individuals</div>
<div class="abs social">
  <span class="social-item">Chirpline</span>
  <span class="social-item">Workvine</span>
  <span class="social-item">Socialine</span>
  <span class="social-item">Tumble</span>
</div>

<nav class="abs main-nav">
  <span>Home</span><span class="sep">|</span><span>About Dr.Halbrook</span><span class="sep">|</span><span>Coaching</span><span class="sep">|</span><span>Leadership Training</span><span class="sep">|</span><span>Psychotherapy</span><span class="sep">|</span><span>Clients</span><span class="sep">|</span><span>Testimonials</span><span class="sep">|</span><span>Contact</span>
</nav>

<section class="abs welcome"></section>
<h1 class="abs welcome-title">Welcome</h1>
<div class="abs welcome-sub">Lorem Ipsum is simply dummy text</div>
<p class="abs welcome-copy">Lorem Ipsum is simply dummy text of the printing and typesetting industry. Lorem Ipsum has been the industry's standard dummy text ever since the 1500s Lorem Ipsum is simply dummy text of the printing and</p>
<div class="abs btn-more">READ MORE
  <svg width="14" height="14" viewBox="0 0 14 14"><circle cx="7" cy="7" r="6" fill="none" stroke="#fff" stroke-width="1.5"/><path d="M5.5 4.5 L9 7 L5.5 9.5Z" fill="#fff"/></svg>
</div>

<div class="abs video-bar">VIDEO</div>
<div class="abs video"></div>
<div class="abs video-frame" role="img" aria-label="Video still of a speaker at a lectern in a meeting room"></div>
<div class="abs video-caption">Peter Halbrook, My Father</div>
<svg class="abs" style="left:775px;top:358px" width="64" height="38" viewBox="0 0 64 38"><rect width="64" height="38" rx="8" fill="#1a1a1a" opacity=".85"/><path d="M26 11 L41 19 L26 27Z" fill="#fff"/></svg>
<div class="abs video-controls">
  <svg class="abs" style="left:0;top:-4px" width="375" height="6"><rect y="2" width="375" height="3" fill="#555"/><circle cx="8" cy="3.5" r="3.5" fill="#ddd"/></svg>
  <svg class="abs" style="left:18px;top:7px" width="12" height="12"><path d="M2 1 L11 6 L2 11Z" fill="#aaa"/></svg>
  <svg class="abs" style="left:52px;top:7px" width="16" height="12"><path d="M1 4 H4 L8 1 V11 L4 8 H1Z" fill="#aaa"/></svg>
  <span class="abs" style="left:80px;top:7px"><b style="color:#fff">0:00</b> / 6:15</span>
  <span class="abs" style="left:286px;top:7px">Vidstream</span>
  <svg class="abs" style="left:344px;top:6px" width="14" height="12"><path d="M1 4V1H4M10 1H13V4M13 8V11H10M4 11H1V8" fill="none" stroke="#aaa" stroke-width="1.5"/></svg>
</div>

<h2 class="abs col-title" style="left:62px;top:556px">Socialine Integration</h2>
<div class="abs like-row"><span class="like-btn">Like</span><span class="network-square"></span><span><span style="color:var(--network-blue)">204,599 people</span> like this.</span></div>
<aside class="abs activity">
  <div class="activity-head">Recent Activity</div>
  <div class="login-row"><span class="login-btn">Login</span><span>You need to be logged into Socialine to see your friends' recent activity.</span></div>
  <div class="act-item"><span class="act-icon" style="background:#8dc63f"></span><span><b>What's New in Release 3</b>272 people recommended this.</span></div>
  <div class="act-item"><span class="act-icon" style="background:#4a66a8"></span><span><b>Share Button</b>114,172 people recommended this.</span></div>
  <div class="act-item"><span class="act-icon" style="background:#2aa6de"></span><span><b>Platform Notes: Building a Kinder Workplace</b>One person recommended this.</span></div>
  <div class="act-item"><span class="act-icon" style="background:#c8d0e0"></span><span><b>Introducing the Partner Resource Hub for Teams</b>103 people recommended this.</span></div>
  <div class="plugin-foot"><span class="network-square"></span>Socialine social plugin</div>
</aside>
<div class="abs divider"></div>

<h2 class="abs col-title" style="left:438px;top:556px">Leadership Training</h2>
<div class="abs service-img" style="left:430px;top:602px;background:linear-gradient(135deg,#f6b07a,#e5743a 50%,#f3c59c)" role="img" aria-label="Warm orange sandstone canyon walls"></div>
<p class="abs service-blurb" style="left:626px;top:603px;width:340px">Creating custom-made leadership workshops to fit the needs of organizations.</p>
<p class="abs service-copy" style="left:626px;top:647px;width:380px">Lorem Ipsum is simply dummy text of the printing and typesetting industry. Lorem Ipsum has been the industry's standard dummy text ever since the 1500s,</p>

<h2 class="abs col-title" style="left:437px;top:728px">Executive Coaching</h2>
<div class="abs service-img" style="left:428px;top:760px;background:linear-gradient(120deg,#f07a2a,#d8541a 60%,#b9441a)" role="img" aria-label="Stack of balanced stones on an orange background"></div>
<p class="abs service-blurb" style="left:629px;top:761px">Partnering with clients one-on-one to actualize their professional potential.</p>
<p class="abs service-copy" style="left:629px;top:806px">Lorem Ipsum is simply dummy text of the printing and typesetting industry. Lorem Ipsum has been the industry's standard dummy text ever since the 1500s</p>

<h2 class="abs col-title" style="left:437px;top:885px">Psychotherapy</h2>
<div class="abs service-img" style="left:428px;top:918px;background:linear-gradient(135deg,#f9a23a,#f2821c 55%,#e86c12)" role="img" aria-label="Raked orange sand garden"></div>
<p class="abs service-blurb" style="left:629px;top:919px">Deepening personal insight and developing behaviors to grow in well-being</p>
<p class="abs service-copy" style="left:629px;top:964px">Lorem Ipsum is simply dummy text of the printing and typesetting industry. Lorem Ipsum has been the industry's standard dummy text ever since the 1500s,</p>

<footer class="abs site-footer">
  <p>Copyright © 2006-2013 HCHalbrook | All rights reserved</p>
  <div class="footer-links">Home <span style="color:#555">|</span> Contact</div>
</footer>

</body>
</html>
```